Sport Celebration Day Poster

The poster should highlight the sport of archery and bring awareness to the sport and invite people to come and try archery. We have a logo that must be featured, as well as a sample photos that can be used in the creative process, but do not necessarily have to be featured. The feel of the poster should be fun and inviting and have archery imagery (bows, arrows, targets, etc.).

The poster must feature the date MAY 11, 2019 and "Try Archery."

We would like to see an area where our sport clubs can fill in their own information including sections for "Name, Date, Location, Times, Location, Email, Website, and Notes."

Submissions should include some of these colours or colours from the logo:
Blue #00A1EF, Grey #313A43, Green #406C1D, Red #DC2F31, Yellow #FDDD39

```html
<!DOCTYPE html>
<html lang="en">
<head>
<meta charset="utf-8">
<title>Fletchfield Day Poster</title>
<link rel="stylesheet" href="https://fonts.googleapis.com/css2?family=Saira+Semi+Condensed:ital,wght@0,700;1,600&family=Montserrat:wght@500;600&display=swap">
<style>
  :root {
    --grey: #313A43;
    --red: #DC2F31;
    --white: #FFFFFF;
    --canvas: #E6E7E8;
    --badge: #C9CDD2;
    --photo-top: #D9D4CF;
    --photo-bottom: #8F7E86;
  }
  html, body {
    margin: 0;
    width: 1200px;
    height: 1000px;
    overflow: hidden;
    background: var(--canvas);
  }
  .poster {
    position: absolute;
    left: 285px;
    top: 34px;
    width: 575px;
    height: 850px;
    transform: scale(1.095);
    transform-origin: top left;
    background: var(--grey);
    overflow: hidden;
  }
  .poster-shapes { position: absolute; inset: 0; }
  .brand {
    position: absolute;
    left: 70px;
    top: 80px;
    display: flex;
    align-items: center;
    gap: 14px;
  }
  .brand-dot {
    width: 46px;
    height: 46px;
    border-radius: 50%;
    background: var(--red);
  }
  .brand-name {
    font-family: "Saira Semi Condensed", sans-serif;
    font-weight: 700;
    font-size: 44px;
    line-height: 0.95;
    color: var(--white);
    text-transform: uppercase;
    letter-spacing: 1px;
  }
  .photo {
    position: absolute;
    left: 170px;
    top: 265px;
    width: 225px;
    height: 385px;
    background: linear-gradient(180deg, var(--photo-top), var(--photo-bottom));
  }
  .invite-box, .fact-box {
    position: absolute;
    background: var(--red);
    color: var(--white);
    display: flex;
    flex-direction: column;
    justify-content: center;
    align-items: center;
  }
  .invite-box {
    left: 0;
    top: 362px;
    width: 172px;
    height: 188px;
    font-family: "Saira Semi Condensed", sans-serif;
    font-style: italic;
    font-weight: 600;
    font-size: 29px;
    line-height: 50px;
    text-align: center;
  }
  .fact-box {
    left: 395px;
    top: 365px;
    width: 178px;
    height: 190px;
    font-family: "Montserrat", sans-serif;
    font-weight: 600;
    font-size: 14px;
    letter-spacing: 2.4px;
    line-height: 42px;
    text-align: center;
  }
  .event-date {
    position: absolute;
    right: 25px;
    top: 674px;
    font-family: "Montserrat", sans-serif;
    font-weight: 600;
    font-size: 26px;
    letter-spacing: 4.5px;
    color: var(--white);
  }
  .partner-strip {
    position: absolute;
    left: 0;
    top: 750px;
    width: 575px;
    height: 76px;
    background: var(--white);
    display: flex;
    align-items: center;
    justify-content: space-around;
  }
  .partner-badge { background: var(--badge); }
  .partner-badge.round { width: 56px; height: 56px; border-radius: 50%; }
  .partner-badge.wide { width: 150px; height: 34px; }
  .partner-badge.mid { width: 96px; height: 44px; }
  .partner-badge.small { width: 78px; height: 36px; }
</style>
</head>
<body>
  <div class="poster">
    <svg class="poster-shapes" viewBox="0 0 575 850" width="575" height="850" aria-hidden="true">
      <g class="target-rings">
        <circle cx="590" cy="-25" r="235" fill="var(--red)"/>
        <circle cx="590" cy="-25" r="190" fill="var(--grey)"/>
        <circle cx="590" cy="-25" r="130" fill="var(--red)"/>
        <circle cx="590" cy="-25" r="70" fill="var(--grey)"/>
      </g>
      <path class="red-swoosh" d="M0,360 Q140,280 300,250 Q440,222 575,220 L575,590 Q300,650 0,680 Z" fill="var(--red)"/>
      <path d="M300,250 Q440,222 575,220" fill="none" stroke="var(--white)" stroke-width="4"/>
      <path d="M0,680 Q300,650 575,590" fill="none" stroke="var(--white)" stroke-width="4"/>
      <ellipse class="photo-frame" cx="287" cy="440" rx="278" ry="215" fill="var(--grey)" stroke="var(--white)" stroke-width="4"/>
      <rect x="0" y="725" width="575" height="15" fill="var(--red)"/>
      <rect x="0" y="832" width="575" height="18" fill="var(--red)"/>
    </svg>

    <div class="brand">
      <div class="brand-dot"></div>
      <div class="brand-name">Fletchfield<br>Day</div>
    </div>

    <div class="photo" role="img" aria-label="Photo of a young archer drawing a bow at an indoor range with targets"></div>

    <div class="invite-box">
      <span>Come</span>
      <span>and try</span>
      <span>an Achery!</span>
    </div>

    <div class="fact-box">
      <span>ONE OF THE</span>
      <span>OLDEST</span>
      <span>SPORTS STILL</span>
      <span>PRACTICED</span>
    </div>

    <div class="event-date">MAY.11, 2019</div>

    <div class="partner-strip">
      <div class="partner-badge round"></div>
      <div class="partner-badge round"></div>
      <div class="partner-badge wide"></div>
      <div class="partner-badge mid"></div>
      <div class="partner-badge small"></div>
    </div>
  </div>
</body>
</html>
```